Sandwich Board-

We need a (3) 24" X 36" PORTRAIT & 8.5 x11" Graphic Panels with a beautiful nature photo, waterfall or some nice photo with river, ponds or lake as background image.

BE SURE TO USE PHOTOS FROM TROPICAL ENVIRONMENTS - NOT WINTER ALPS ETC

Designer to find & select (2) photos to be used. (1) photo for each poster

I will pay for photos if required from photo licensing site

Poster is an Invitation to attend: "Velvet Ember Music Event" ( see attached photo)

Details of Event: see attached photo ( LEAVE OUT ADDRESS)

I PROVIDED A REAL ROUGH DRAFT AS A SAMPLE

Requirements
Must have
• The following text must be on each design
• 1. 412 Maneola rd. Pahoa
• 2. No Charge or Free Event
• 3. Every Sunday
• 4. Ph: 808.555.0193

```html
<!DOCTYPE html>
<html lang="en">
<head>
<meta charset="utf-8">
<title>Velvet Ember Music Event</title>
<link rel="stylesheet" href="https://fonts.googleapis.com/css2?family=Josefin+Sans:wght@300;400&family=Great+Vibes&family=Arimo:wght@700&display=swap">
<style>
  :root {
    --sky: #6a7178;
    --mountain: #59636f;
    --forest-deep: #1c261e;
    --forest-mid: #263226;
    --meadow: #414d2e;
    --meadow-dark: #2b3422;
    --ink: #ffffff;
    --ink-soft: rgba(255,255,255,0.88);
  }
  html, body {
    margin: 0;
    padding: 0;
    overflow: hidden;
    background: #1b221c;
  }
  .poster {
    position: relative;
    width: 800px;
    height: 1200px;
    overflow: hidden;
  }
  .poster__backdrop {
    position: absolute;
    inset: 0;
    background:
      radial-gradient(ellipse 30% 10% at 42% 22%, rgba(150,158,170,0.45), transparent 70%),
      radial-gradient(ellipse 22% 40% at 6% 45%, rgba(14,20,15,0.7), transparent 75%),
      radial-gradient(ellipse 22% 40% at 94% 45%, rgba(14,20,15,0.7), transparent 75%),
      radial-gradient(ellipse 40% 16% at 25% 82%, rgba(92,96,52,0.5), transparent 75%),
      radial-gradient(ellipse 40% 16% at 78% 86%, rgba(84,92,50,0.45), transparent 75%),
      linear-gradient(180deg,
        var(--sky) 0%,
        #5a6166 12%,
        var(--mountain) 22%,
        #3a4640 30%,
        var(--forest-mid) 38%,
        var(--forest-deep) 55%,
        #2a3424 66%,
        var(--meadow) 80%,
        var(--meadow-dark) 100%);
  }
  .poster__frames {
    position: absolute;
    inset: 0;
  }
  .poster__content {
    position: absolute;
    inset: 0;
    color: var(--ink);
    text-align: center;
  }
  .poster__content > * {
    position: absolute;
    left: 0;
    right: 0;
    margin: 0;
  }
  .event-title {
    top: 448px;
    font-family: "Josefin Sans", sans-serif;
    font-weight: 400;
    font-size: 34px;
    letter-spacing: 3.2px;
    text-transform: uppercase;
  }
  .event-subtitle {
    top: 488px;
    font-family: "Josefin Sans", sans-serif;
    font-weight: 300;
    font-size: 19px;
    letter-spacing: 1.6px;
    text-transform: uppercase;
    color: var(--ink-soft);
  }
  .featuring-label {
    top: 606px;
    font-family: "Josefin Sans", sans-serif;
    font-weight: 300;
    font-size: 14px;
    color: var(--ink-soft);
  }
  .performer-name {
    top: 622px;
    font-family: "Great Vibes", cursive;
    font-weight: 400;
    font-size: 56px;
    line-height: 1.2;
  }
  .event-schedule {
    top: 852px;
    font-family: "Arimo", sans-serif;
    font-weight: 700;
    font-size: 25px;
  }
  .event-admission {
    top: 900px;
    font-family: "Josefin Sans", sans-serif;
    font-weight: 400;
    font-size: 16px;
    letter-spacing: 2px;
    text-transform: uppercase;
    color: var(--ink-soft);
  }
  .event-address {
    top: 928px;
    font-family: "Josefin Sans", sans-serif;
    font-weight: 300;
    font-size: 16px;
    letter-spacing: 1.2px;
    color: var(--ink-soft);
  }
  .event-contact {
    top: 1090px;
    font-family: "Josefin Sans", sans-serif;
    font-weight: 300;
    font-size: 15px;
    letter-spacing: 1.5px;
    color: var(--ink-soft);
  }
</style>
</head>
<body>
  <main class="poster">
    <div class="poster__backdrop" role="img" aria-label="Nature photo background: tall evergreen trees framing a distant peak under a grey sky, with a wildflower meadow and a small stream below"></div>

    <svg class="poster__frames" width="800" height="1200" viewBox="0 0 800 1200" aria-hidden="true">
      <g fill="none" stroke="#ffffff" stroke-width="2">
        <rect x="33" y="33" width="702" height="1100"/>
        <rect x="67" y="67" width="700" height="1100"/>
      </g>
      <g fill="none" stroke="#ffffff" stroke-width="0.8" opacity="0.85">
        <polygon points="400,532 700,663 400,794 100,663"/>
        <polygon points="408,536 694,660 408,790 106,666"/>
        <polygon points="392,536 106,660 392,790 694,666"/>
        <polygon points="400,540 688,663 400,786 112,663"/>
      </g>
    </svg>

    <section class="poster__content">
      <h1 class="event-title">Velvet Ember Music Event</h1>
      <p class="event-subtitle">Chanting, Dancing, &amp; Feasting</p>
      <p class="featuring-label">featuring</p>
      <p class="performer-name">Kaimana Lila Rose</p>
      <p class="event-schedule">every SUNDAY&nbsp; at 6PM</p>
      <p class="event-admission">No Charge &middot; Free Event</p>
      <p class="event-address">412 Maneola rd. Pahoa</p>
      <p class="event-contact">for more information, please call Ph: 808.555.0193</p>
    </section>
  </main>
</body>
</html>
```